New Business Cards for Velmora

About Velmora:
At Velmora, we're more than just a company—we're a force for positive change in the staffing industry. Our brand is our heartbeat, and we need a designer who can translate that into every design element.

The Project:
We're revamping our business cards and need your artistic flair to make them stand out. Here's what we're looking for:

- Incorporate our existing brand elements (logo, colours, fonts) into the design.
- Craft a design that's sleek, professional, and memorable.
- Provide options for different layouts and finishes.
- Collaborate closely with our team to ensure the final product exceeds expectations.

Please note: For general text, we use Avenir. The brand guidelines are slightly out of date and don't have correct imaging. Colours are correct though.

```html
<!DOCTYPE html>
<html lang="en">
<head>
<meta charset="utf-8">
<title>Velmora Business Cards</title>
<link href="https://fonts.googleapis.com/css2?family=Montserrat:wght@700&family=Nunito+Sans:wght@400;600;700&display=swap" rel="stylesheet">
<style>
  :root {
    --backdrop: #f1f1f2;
    --card: #ffffff;
    --navy: #1d3352;
    --plum: #6a2f78;
    --magenta: #d93a7c;
    --white: #ffffff;
  }
  * { box-sizing: border-box; margin: 0; padding: 0; }
  html, body { width: 1200px; height: 1200px; overflow: hidden; }
  body {
    background: var(--backdrop);
    font-family: "Nunito Sans", sans-serif;
    position: relative;
  }
  .card {
    position: absolute;
    left: 154px;
    width: 894px;
    height: 535px;
    background: var(--card);
    box-shadow: 0 4px 14px rgba(0, 0, 0, 0.12);
    overflow: hidden;
  }
  .card--front { top: 44px; }
  .card--back { top: 612px; }

  .corner-tab {
    position: absolute;
    left: 50px;
    top: 0;
    width: 64px;
    height: 164px;
    border-bottom-right-radius: 64px;
    background: linear-gradient(180deg, var(--plum), var(--magenta));
  }
  .holder { position: absolute; left: 50px; top: 196px; color: var(--navy); }
  .holder__name {
    font-family: "Montserrat", sans-serif;
    font-weight: 700;
    font-size: 36px;
    line-height: 46px;
    letter-spacing: 0.3px;
  }
  .holder__role { font-size: 21px; line-height: 28px; margin-top: 2px; letter-spacing: 0.4px; }

  .address {
    position: absolute;
    left: 50px;
    top: 422px;
    display: flex;
    gap: 14px;
    color: var(--navy);
    font-size: 21px;
    font-style: normal;
    line-height: 29px;
    letter-spacing: 0.4px;
  }
  .address svg { margin-top: 6px; flex: none; }

  .contact-band {
    position: absolute;
    left: 386px;
    top: 364px;
    width: 508px;
    height: 128px;
    border-top-left-radius: 130px 128px;
    background: linear-gradient(90deg, var(--magenta), var(--plum));
    color: var(--white);
  }
  .contact-band ul { list-style: none; position: absolute; right: 22px; top: 26px; }
  .contact-band li {
    display: flex;
    justify-content: flex-end;
    align-items: center;
    gap: 12px;
    font-size: 21px;
    line-height: 28px;
    letter-spacing: 0.5px;
  }
  .contact-band svg { width: 16px; height: 16px; flex: none; }

  .brand { position: absolute; text-align: center; color: var(--plum); }
  .brand__name { font-weight: 700; line-height: 1; letter-spacing: 0.5px; }
  .brand__tagline { font-weight: 400; color: var(--plum); }

  .brand--small { left: 440px; top: 66px; width: 400px; }
  .brand--small .brand__name { font-size: 64px; }
  .brand--small .brand__tagline { font-size: 20px; margin-top: 8px; }

  .brand--large { left: 0; top: 170px; width: 894px; }
  .brand--large .brand__name { font-size: 120px; }
  .brand--large .brand__tagline { font-size: 34px; margin-top: 14px; }
</style>
</head>
<body>
  <section class="card card--front">
    <div class="corner-tab"></div>

    <div class="brand brand--small">
      <p class="brand__name">Velmora</p>
      <p class="brand__tagline">people first, always</p>
    </div>

    <div class="holder">
      <h1 class="holder__name">Marcus<br>Delaney</h1>
      <p class="holder__role">Founder &amp; Director</p>
    </div>

    <address class="address">
      <svg width="12" height="16" viewBox="0 0 12 16" aria-hidden="true"><path d="M6 0a6 6 0 0 0-6 6c0 4.5 6 10 6 10s6-5.5 6-10a6 6 0 0 0-6-6zm0 8.2A2.2 2.2 0 1 1 6 3.8a2.2 2.2 0 0 1 0 4.4z" fill="var(--navy)"/></svg>
      <span>7/B, Linden Row<br>Pin - 482019</span>
    </address>

    <div class="contact-band">
      <ul>
        <li>5550-214-377
          <svg viewBox="0 0 16 16" aria-hidden="true"><path d="M3.6 1.2l2.2 2.6-1.3 1.7a9 9 0 0 0 6 6l1.7-1.3 2.6 2.2-1.4 2.2C7.3 14.6 1.4 8.7 1.4 2.6z" fill="var(--white)"/></svg>
        </li>
        <li>info@mdpartners.com
          <svg viewBox="0 0 16 16" aria-hidden="true"><rect x="1" y="3" width="14" height="10" rx="1" fill="var(--white)"/><path d="M1.5 3.5L8 9l6.5-5.5" stroke="var(--plum)" stroke-width="1.2" fill="none"/></svg>
        </li>
        <li>www.mdpartners.com
          <svg viewBox="0 0 16 16" aria-hidden="true"><circle cx="8" cy="8" r="6.5" fill="none" stroke="var(--white)" stroke-width="1.4"/><ellipse cx="8" cy="8" rx="2.8" ry="6.5" fill="none" stroke="var(--white)" stroke-width="1.2"/><path d="M1.5 8h13" stroke="var(--white)" stroke-width="1.2"/></svg>
        </li>
      </ul>
    </div>
  </section>

  <section class="card card--back">
    <div class="brand brand--large">
      <p class="brand__name">Velmora</p>
      <p class="brand__tagline">people first, always</p>
    </div>
  </section>
</body>
</html>
```